Pebblewick - a new nut butter brand in Switzerland

We are launching a new and innovative line of organic Nut Butters in Switzerland called Pebblewick. 340g round glass jar and require a cool label design for the front, back and top of the jar. Pebblewick soldier and our slogan is "Seeds from every far shore - tended in Zurich". It must therefore include the "flavor". The back label wants to include product description and nutritional information. The top should include the brand name, flavor and maybe another image. Overall we want to convey a young and fun designs appealing to the local hipster movement. The label designs we like are Gilroy's Spread, Marla's and Mango Haven.

Target Market(s)

Swiss hipster commutity

Industry/Entity Type

Food Production

Font styles to use
Sans Serif

Colors
85cae6
86cfc6
cadf82
fbf289
fee18a
f8ba93
f9ba93
f59296
eea4c8

Requirements
Must have
• "Almond butter" on the front. A graphic representation of a Pebblewick that will serve as our logo - clean and fun (refer to mango haven) in large font "Seeds from every far shore - tended in Zurich" on the front; slightly smaller than the "Almond Butter"
Nice to have

```html
<!DOCTYPE html>
<html lang="en">
<head>
<meta charset="utf-8">
<title>Pebblewick – Almond Butter Label</title>
<link rel="stylesheet" href="https://fonts.googleapis.com/css2?family=Fredoka:wght@500&family=Questrial&family=Merienda:wght@400&family=Arimo:wght@400;700&display=swap">
<style>
  :root {
    --bg-light: #fbfbfb;
    --bg-edge: #dcdde0;
    --brown: #8a5b3a;
    --brown-soft: #c8ad8f;
    --sand: #e4ddcf;
    --ink: #1c1c1c;
    --white: #ffffff;
    --tm: #8a5b3a;
  }
  html, body {
    margin: 0;
    padding: 0;
    overflow: hidden;
  }
  .label {
    position: relative;
    width: 1200px;
    height: 962px;
    overflow: hidden;
    background: radial-gradient(ellipse 70% 65% at 52% 52%, var(--bg-light) 0%, #f1f1f2 45%, var(--bg-edge) 100%);
  }
  .flavour-band {
    position: absolute;
    left: 344px;
    top: 608px;
    width: 848px;
    height: 84px;
    background: linear-gradient(90deg, rgba(228,221,207,0.2) 0%, var(--brown-soft) 6%, var(--brown) 20%, var(--brown) 66%, var(--brown-soft) 84%, var(--sand) 100%);
  }
  .flavour-band__text {
    position: absolute;
    left: 146px;
    top: 9px;
    margin: 0;
    font-family: "Merienda", cursive;
    font-size: 44px;
    color: var(--white);
    letter-spacing: 0.5px;
    white-space: nowrap;
  }
  .soldier-art {
    position: absolute;
    left: 48px;
    top: 36px;
    width: 384px;
    height: 878px;
  }
  .brand {
    position: absolute;
    left: 456px;
    top: 130px;
    width: 600px;
    margin: 0;
    text-align: center;
    font-family: "Fredoka", sans-serif;
    font-weight: 500;
    color: var(--brown);
    font-size: 168px;
    line-height: 140px;
  }
  .brand__line {
    display: block;
  }
  .brand__tm {
    position: absolute;
    left: 1024px;
    top: 196px;
    font-family: "Questrial", sans-serif;
    font-size: 30px;
    line-height: 1;
    color: var(--tm);
  }
  .slogan {
    position: absolute;
    left: 406px;
    top: 468px;
    width: 700px;
    margin: 0;
    text-align: center;
    font-family: "Questrial", sans-serif;
    font-size: 31px;
    line-height: 1.2;
    color: var(--ink);
    white-space: nowrap;
  }
  .net-weight {
    position: absolute;
    left: 588px;
    top: 808px;
    width: 336px;
    height: 336px;
    border-radius: 50%;
    background: var(--brown);
    color: var(--white);
    text-align: center;
    font-family: "Arimo", sans-serif;
  }
  .net-weight__label {
    margin: 44px 0 0;
    font-family: "Questrial", sans-serif;
    font-size: 32px;
    line-height: 1;
  }
  .net-weight__value {
    margin: 16px 0 0;
    font-size: 38px;
    line-height: 1;
  }
  .net-weight__value strong {
    font-weight: 700;
  }
</style>
</head>
<body>
  <main class="label">
    <div class="flavour-band">
      <p class="flavour-band__text">Almond Butter</p>
    </div>

    <svg class="soldier-art" role="img" aria-label="Illustration of the Pebblewick soldier mascot with crested helmet, cape and sword, standing on a round grey base" viewBox="0 0 384 878">
      <defs>
        <linearGradient id="soldier-tones" x1="0" y1="0" x2="0" y2="1">
          <stop offset="0" stop-color="#e9d2bf"/>
          <stop offset="0.45" stop-color="#f5e6da"/>
          <stop offset="0.8" stop-color="#e6d3c3"/>
          <stop offset="1" stop-color="#d9d9dc"/>
        </linearGradient>
      </defs>
      <rect x="0" y="0" width="384" height="878" rx="24" fill="url(#soldier-tones)"/>
    </svg>

    <h1 class="brand">
      <span class="brand__line">Pebble</span>
      <span class="brand__line">wick</span>
    </h1>
    <span class="brand__tm">TM</span>

    <p class="slogan">Seeds from every far shore - tended in Zurich</p>

    <div class="net-weight">
      <p class="net-weight__label">Net Weight</p>
      <p class="net-weight__value"><strong>340</strong>g</p>
    </div>
  </main>
</body>
</html>
```